Varindel Homes needs a stationery design

I need a stationary design for my new custom home building company. Our company deals with very high end and luxurious homes so i need a stationary design that shows strength, elegance, and trust.
The final version should be trendy, clean... only 2 colours (green + grey/black) and professional.
#1: Business Cards (design on 2 sides)
#2: Letterhead (word format)
#3: Cover Page and back cover for proposals
#4: Envelopes,
#5: Thank You card,
#6: Presentation Folder
Logo is attached. Logo can be reversed out (will attach once available). Logo can be stacked or horizontal (provided as horizontal).
The business cards need to be two sided with the company logo and website on the front (www.varindelhomes-demo.net and contact info on the back.
The contact info can be made up temporarily and once the final design is chosen, i will provide you with all the correct contact information during the revision stage.
id like to see examples with black, white, blue, red, purple. (You should not try to use all these in one design)
I have attached my company's logo in 3 different colours and a few sample business cards that i found on the internet. I would like to see unique designs though, don't try to imitate the examples
Updates
Dear designers,
I have also attached the .eps and ai files for the 3 different coloured logos.
Please notify me if you need anything else to complete your work
Best Regards,
Varindel

```html
<!DOCTYPE html>
<html lang="en">
<head>
<meta charset="UTF-8">
<title>Varindel Homes – Stationery Set</title>
<link href="https://fonts.googleapis.com/css2?family=Lato:wght@400;700;900&display=swap" rel="stylesheet">
<style>
  :root{
    --bg:#f1f1f1;
    --paper:#ffffff;
    --card-grey:#e7e7e7;
    --green:#0a8f45;
    --green-dark:#0b6b36;
    --charcoal:#2f2f2f;
    --grey:#8a8a8a;
    --ink:#1e1e1e;
    --shadow:3px 5px 8px rgba(0,0,0,.45);
  }
  *{box-sizing:border-box;margin:0;padding:0}
  html,body{width:1200px;height:1000px;overflow:hidden;background:var(--bg);font-family:"Lato",sans-serif;color:var(--ink)}
  .canvas{position:relative;width:1200px;height:1000px}
  .sheet{position:absolute;background:var(--paper);box-shadow:var(--shadow);overflow:hidden}

  .band-green{position:absolute;left:0;right:0;background:linear-gradient(90deg,var(--green-dark),var(--green) 50%,var(--green-dark))}
  .band-dark{position:absolute;left:0;right:0;background:var(--charcoal)}
  .band-grey{position:absolute;left:0;right:0;background:linear-gradient(90deg,var(--charcoal),var(--grey))}

  .brand{display:flex;align-items:center;gap:.35em;color:#3a3a3a;font-weight:900;letter-spacing:.06em;text-transform:uppercase;white-space:nowrap;line-height:1}
  .brand-mark{width:.7em;height:.7em;background:#3a3a3a;flex:none}

  /* square card */
  .square-card{left:142px;top:78px;width:288px;height:290px;border-radius:12px}
  .square-card .brand{position:absolute;left:0;right:0;top:134px;justify-content:center;font-size:25px}

  /* envelope */
  .envelope{left:30px;top:448px;width:503px;height:252px}
  .envelope .brand{position:absolute;left:26px;top:32px;font-size:11px}
  .address{position:absolute;font-size:10px;line-height:12px}
  .sender{left:25px;top:64px}
  .receiver{left:207px;top:127px}

  /* letterhead */
  .letterhead{left:565px;top:112px;width:610px;height:791px}
  .letterhead .brand{position:absolute;left:26px;top:52px;font-size:20px}
  .lh-info{position:absolute;left:313px;width:200px;top:25px;text-align:center;font-size:10px;line-height:12px}
  .lh-info .name{font-weight:700;font-size:12px;letter-spacing:.2em;margin-bottom:2px}

  /* business cards */
  .biz-card{top:777px;width:252px;height:144px;border-radius:10px;background:var(--card-grey)}
  .biz-front{left:25px}
  .biz-back{left:288px;top:773px}
  .biz-card svg{position:absolute;left:0;top:0}
  .biz-front .brand{position:absolute;left:0;right:0;top:74px;justify-content:center;font-size:15px}
  .biz-front .web{position:absolute;left:0;right:0;top:103px;text-align:center;font-size:7px;letter-spacing:.16em;color:#333}
  .biz-back .brand{position:absolute;left:8px;top:86px;font-size:8px}
  .holder{position:absolute;left:100px;width:160px;text-align:center;top:51px;font-size:8px}
  .holder-sub{position:absolute;left:100px;width:160px;text-align:center;top:68px;font-size:6px}
  .contact{position:absolute;left:103px;top:83px;border-collapse:collapse;font-size:6px}
  .contact td{padding:0 0 2.5px 0;line-height:7px}
  .contact td:first-child{width:72px}
</style>
</head>
<body>
<div class="canvas">

  <!-- Square card -->
  <div class="sheet square-card">
    <div class="band-green" style="top:0;height:14px"></div>
    <div class="band-grey" style="top:14px;height:7px"></div>
    <div class="brand"><span class="brand-mark"></span>Varindel Homes</div>
    <div class="band-grey" style="top:268px;height:6px"></div>
    <div class="band-green" style="top:274px;height:16px"></div>
  </div>

  <!-- Envelope -->
  <div class="sheet envelope">
    <div class="band-green" style="top:0;height:12px"></div>
    <div class="band-dark" style="top:12px;height:6px"></div>
    <div class="brand"><span class="brand-mark"></span>Varindel Homes</div>
    <div class="address sender">Sender's Name<br>Company Address</div>
    <div class="address receiver">Reciever's Name<br>Mail Address<br>Contact Info</div>
    <div class="band-grey" style="top:232px;height:6px"></div>
    <div class="band-green" style="top:238px;height:14px"></div>
  </div>

  <!-- Letterhead -->
  <div class="sheet letterhead">
    <div class="brand"><span class="brand-mark"></span>Varindel Homes</div>
    <div class="lh-info">
      <div class="name">VARINDEL HOMES</div>
      <div>Company Address</div>
      <div>Contact</div>
      <div>Website</div>
    </div>
    <div class="band-green" style="top:99px;height:5px"></div>
    <div class="band-grey" style="top:106px;height:3px"></div>
  </div>

  <!-- Business card front -->
  <div class="sheet biz-card biz-front">
    <svg width="252" height="144" viewBox="0 0 252 144" aria-hidden="true">
      <defs>
        <linearGradient id="gf" x1="0" x2="1"><stop offset="0" stop-color="#0b6b36"/><stop offset=".5" stop-color="#0a8f45"/><stop offset="1" stop-color="#0b6b36"/></linearGradient>
      </defs>
      <path d="M0 0H252V22C200 14 160 38 100 34C60 31 30 22 0 26Z" fill="url(#gf)"/>
      <path d="M0 26C30 22 60 31 100 34C160 38 200 14 252 22V27C200 19 160 43 100 39C60 36 30 27 0 31Z" fill="#2f2f2f"/>
      <rect y="126" width="252" height="5" fill="#2f2f2f"/>
      <rect y="131" width="252" height="13" fill="url(#gf)"/>
    </svg>
    <div class="brand"><span class="brand-mark"></span>Varindel Homes</div>
    <div class="web">www.varindelhomes-demo.net</div>
  </div>

  <!-- Business card back -->
  <div class="sheet biz-card biz-back">
    <svg width="252" height="144" viewBox="0 0 252 144" aria-hidden="true">
      <defs>
        <linearGradient id="gb" x1="0" x2="1"><stop offset="0" stop-color="#0b6b36"/><stop offset=".5" stop-color="#0a8f45"/><stop offset="1" stop-color="#0b6b36"/></linearGradient>
      </defs>
      <path d="M0 0H252V26C200 24 170 42 110 34C70 28 40 20 0 30Z" fill="url(#gb)"/>
      <path d="M0 30C40 20 70 28 110 34C170 42 200 24 252 26V32C200 30 170 48 110 40C70 34 40 26 0 36Z" fill="#2f2f2f"/>
      <rect y="126" width="252" height="5" fill="#2f2f2f"/>
      <rect y="131" width="252" height="13" fill="url(#gb)"/>
    </svg>
    <div class="brand"><span class="brand-mark"></span>Varindel Homes</div>
    <div class="holder">MAREN TOLLIS</div>
    <div class="holder-sub">Company or Personal Address</div>
    <table class="contact">
      <tr><td>Phone No.:</td><td>xxx - xxx - xxxx</td></tr>
      <tr><td>Fax No.:</td><td>xxx - xxx - xxxx</td></tr>
      <tr><td>Email Address:</td><td>xxx@xxx.com</td></tr>
      <tr><td>Website:</td><td>www.varindelhomes-demo.net</td></tr>
    </table>
  </div>

</div>
</body>
</html>
```